Clearwave Motion Florida Billboard

We need a billboard designed for our physical therapy practice. Our billboard also serves as the sign for our building. We would like to have some sort of graphic notifying people driving by that our building is located here. Please go to www.clearwavemotionfl.example in order to get a better idea of our company.

Target Market(s)

Senior citizens having physical therapy

Industry/Entity Type

Healthcare- Physical Therapy

Colors
0094D4
00A9DD
6FCCEA
C7EBF8
E9F6FB

Requirements
Must have
• Must contain in bold the words "physical therapy". Must be highly visible from the road and have our company colors incorporated. Would also like to use the phrase "Relieving Pain. Restoring Function. Improving Lives."

```html
<!DOCTYPE html>
<html lang="en">
<head>
<meta charset="utf-8">
<title>Clearwave Motion Florida Billboard</title>
<link rel="stylesheet" href="https://fonts.googleapis.com/css2?family=Montserrat:wght@500;700;800&display=swap">
<style>
  :root {
    --backdrop: #6b6b6b;
    --board-white: #ffffff;
    --sky-tint: #c7ebf8;
    --brand-green: #9dc33b;
    --brand-blue: #4aa8e0;
    --text-grey: #5b5b5b;
    --text-dark: #4a4a4a;
    --rule-grey: #9a9a9a;
  }
  * { margin: 0; padding: 0; box-sizing: border-box; }
  html, body {
    width: 929px;
    height: 1200px;
    overflow: hidden;
    background: var(--backdrop);
    font-family: "Montserrat", sans-serif;
  }
  .billboard {
    position: absolute;
    left: 24px;
    top: 453px;
    width: 880px;
    height: 294px;
    overflow: hidden;
    background:
      radial-gradient(ellipse 420px 260px at 0 0, var(--sky-tint) 0%, rgba(233,246,251,0.6) 45%, rgba(255,255,255,0) 100%),
      var(--board-white);
  }
  .billboard__art {
    position: absolute;
    inset: 0;
    width: 100%;
    height: 100%;
  }
  .headline {
    position: absolute;
    font-weight: 800;
    font-size: 57px;
    line-height: 1;
    letter-spacing: -0.5px;
  }
  .headline--physical { left: 25px; top: 31px; color: var(--brand-green); }
  .headline--therapy { left: 55px; top: 84px; color: var(--brand-blue); }
  .headline-rule {
    position: absolute;
    left: 318px;
    top: 37px;
    width: 1.5px;
    height: 102px;
    background: var(--rule-grey);
  }
  .taglines {
    position: absolute;
    left: 331px;
    top: 39px;
    list-style: none;
    font-weight: 700;
    font-size: 18px;
    line-height: 32px;
    color: var(--text-grey);
  }
  .brand {
    position: absolute;
    left: 28px;
    top: 212px;
    display: flex;
    align-items: center;
    height: 50px;
  }
  .brand__dot {
    width: 48px;
    height: 48px;
    border-radius: 50%;
    background: var(--brand-blue);
  }
  .brand__rule {
    width: 1.5px;
    height: 50px;
    background: var(--text-dark);
    margin: 0 8px 0 6px;
  }
  .brand__name {
    font-weight: 500;
    font-size: 11.5px;
    line-height: 15px;
    letter-spacing: 1px;
    color: var(--text-dark);
    text-transform: uppercase;
  }
  .contact-icon {
    position: absolute;
  }
  .contact-icon--phone { left: 200px; top: 211px; width: 26px; height: 26px; }
  .contact-icon--web { left: 209px; top: 244px; width: 16px; height: 16px; }
  .contact__phone {
    position: absolute;
    left: 237px;
    top: 207px;
    font-weight: 700;
    font-size: 31px;
    line-height: 1;
    color: var(--text-grey);
  }
  .contact__web {
    position: absolute;
    left: 237px;
    top: 242px;
    font-weight: 700;
    font-size: 15.5px;
    line-height: 1;
    color: var(--text-grey);
  }
</style>
</head>
<body>
  <main class="billboard">
    <svg class="billboard__art" viewBox="0 0 1485 495" preserveAspectRatio="none">
      <defs>
        <linearGradient id="photoTone" x1="0" y1="0" x2="1" y2="1">
          <stop offset="0" stop-color="#d9dcdf"/>
          <stop offset="0.5" stop-color="#eef0f2"/>
          <stop offset="1" stop-color="#a9b6c8"/>
        </linearGradient>
      </defs>
      <polygon class="photo-area" role="img" aria-label="Photo of smiling senior patients exercising with hand weights, supported by a physical therapist" points="1000,0 1485,0 1485,495 872,495" fill="url(#photoTone)"/>
      <line class="accent-stripe accent-stripe--blue" x1="947" y1="92" x2="865" y2="403" stroke="var(--brand-blue)" stroke-width="9"/>
      <line class="accent-stripe accent-stripe--green" x1="993" y1="12" x2="865" y2="492" stroke="var(--brand-green)" stroke-width="9"/>
    </svg>

    <h1 class="headline headline--physical">Physical</h1>
    <div class="headline headline--therapy">Therapy</div>
    <div class="headline-rule"></div>

    <ul class="taglines">
      <li>Relieving Pain</li>
      <li>Restoring Function</li>
      <li>Improving Lives</li>
    </ul>

    <div class="brand">
      <span class="brand__dot"></span>
      <span class="brand__rule"></span>
      <span class="brand__name">Clearwave<br>Motion<br>Florida</span>
    </div>

    <svg class="contact-icon contact-icon--phone" viewBox="0 0 24 24" fill="none" stroke="var(--brand-blue)" stroke-width="1.4" stroke-linecap="round" stroke-linejoin="round">
      <path d="M6 3h3l1.5 4-2 1.3a11 11 0 0 0 6.2 6.2l1.3-2 4 1.5v3a2 2 0 0 1-2 2A16 16 0 0 1 4 5a2 2 0 0 1 2-2z"/>
      <path d="M14 3.5a6.5 6.5 0 0 1 6.5 6.5"/>
      <path d="M14 7a3 3 0 0 1 3 3"/>
    </svg>
    <div class="contact__phone">941-555-0176</div>

    <svg class="contact-icon contact-icon--web" viewBox="0 0 24 24" fill="none" stroke="var(--brand-green)" stroke-width="2.4">
      <circle cx="12" cy="12" r="10"/>
      <ellipse cx="12" cy="12" rx="4.5" ry="10"/>
      <line x1="2" y1="12" x2="22" y2="12"/>
    </svg>
    <div class="contact__web">clearwavemotionfl.example</div>
  </main>
</body>
</html>
```